Business Card Design

Attached is my current Business card I do not like it but I must save the logo portion of it. Don't like the color or the lettering am looking for more architectural look in grays or taupe with the green more of a charturese color and the blue a charcoal color on a textured paper that looks more like something high-end that would appeal to an architect or a designer. We make concrete decorative items such as concrete fireplaces, sinks, tops and more.

Target Market(s)

Architects designers of Commercial and Residential - artistic features

Industry/Entity Type

Architect

Contact Information for Business Card

Marla T. Quinby President and Marketing Director
602-471-8836
email marla@quillstoneworks.example
Showroom "Valtique Design Center" 4128 W Larkmoor Scottsdale AZ
Fax: 602-713-4429

Font styles to use
Sans Serif

Requirements
Must have
• Architectural
Natural and earthy colors with a touch of color in the existing attached

```html
<!DOCTYPE html>
<html lang="en">
<head>
<meta charset="utf-8">
<title>Quillstone Works – Business Card</title>
<link rel="stylesheet" href="https://fonts.googleapis.com/css2?family=Play:wght@400;700&display=swap">
<style>
  :root {
    --backdrop: #ece7e0;
    --paper: #f4f4f2;
    --paper-grain: #e9e9e6;
    --ink: #5c6466;
    --ink-soft: #6b7274;
    --accent: #f0c48e;
  }
  * { box-sizing: border-box; margin: 0; padding: 0; }
  html, body {
    width: 1200px;
    height: 1042px;
    overflow: hidden;
    background: var(--backdrop);
    font-family: "Play", sans-serif;
    color: var(--ink);
  }
  .sheet { position: relative; width: 1200px; height: 1042px; }
  .card {
    position: absolute;
    width: 720px;
    height: 420px;
    background:
      repeating-linear-gradient(0deg, var(--paper) 0 2px, var(--paper-grain) 2px 3px),
      var(--paper);
    box-shadow: 0 4px 14px rgba(0,0,0,0.15);
  }
  .card--front { left: 90px; top: 80px; }
  .card--back { left: 360px; top: 520px; }

  .brand {
    position: absolute;
    left: 0; right: 0; top: 120px;
    text-align: center;
  }
  .brand__mark {
    display: block;
    width: 60px; height: 60px;
    margin: 0 auto 24px;
    background: var(--accent);
  }
  .brand__name {
    font-size: 56px;
    line-height: 1;
    color: var(--ink);
  }
  .brand__tagline {
    margin-top: 10px;
    font-size: 24px;
    letter-spacing: 4px;
    color: var(--ink);
  }

  .back-mark {
    position: absolute;
    left: 330px; top: 110px;
    width: 60px; height: 60px;
    background: var(--accent);
  }
  .person {
    position: absolute;
    left: 32px; bottom: 44px;
  }
  .person__name { font-size: 30px; letter-spacing: 1px; color: var(--ink); }
  .person__title { margin-top: 8px; font-size: 15px; letter-spacing: 0.5px; color: var(--ink-soft); }
  .contact {
    position: absolute;
    right: 40px; bottom: 30px;
    text-align: right;
    font-size: 16px;
    line-height: 23px;
    color: var(--ink-soft);
    font-style: normal;
  }
</style>
</head>
<body>
<main class="sheet">
  <section class="card card--front" aria-label="Card front">
    <div class="brand">
      <span class="brand__mark" aria-hidden="true"></span>
      <div class="brand__name">Quillstone Works</div>
      <div class="brand__tagline">Design Studio</div>
    </div>
  </section>

  <section class="card card--back" aria-label="Card back">
    <span class="back-mark" aria-hidden="true"></span>
    <div class="person">
      <div class="person__name">Marla T. Quinby</div>
      <div class="person__title">President and Marketing Director</div>
    </div>
    <address class="contact">
      Showroom "Valtique Design Center"<br>
      4128 W Larkmoor, Halvern Ridge, QL<br>
      marla@quillstoneworks.example<br>
      Call 602-471-8836&nbsp;&nbsp;Fax 602-713-4429
    </address>
  </section>
</main>
</body>
</html>
```